International Tour Operator Needs A New Brochure

We are a newly set up small tour operator focusing on personal tailor made honeymoons for our guests.

We would like to see our logo incorporated into the brochure design as well as our website: marthabellvoyages.co.uk; our e-mail address simon@marthabellvoyages.co.uk; and our mobile number +44 (0)7841296530.

Where as the logo is required, the content in the word document does not have to be used/included. It is there to provide background information on what we do.

The final design should be professional, clear/not crowded, attention grabbing and fit the industry and target segment (brides and grooms).

Target Market(s)

Brides and grooms

Industry/Entity Type

Industry

Colors

Designer to choose colors to be used in the design.

Requirements
Must have
• Logo
Nice to have
• Some content from the word document

```html
<!DOCTYPE html>
<html lang="en">
<head>
<meta charset="utf-8">
<title>Martha Bell Voyages – Brochure</title>
<link href="https://fonts.googleapis.com/css2?family=Poiret+One&family=Arimo:wght@400&family=Tinos:ital@1&display=swap" rel="stylesheet">
<style>
:root{
  --bg:#f1ede6;
  --paper:#ffffff;
  --green-dark:#4a6b5f;
  --green-lite:#9bc23c;
  --body:#7b8984;
  --fold:#e2c9a4;
  --band:#9aaba3;
  --heart-edge:#e6e6e6;
  --photo-a:#cfc3b3;
  --photo-b:#8d9b8a;
}
*{margin:0;padding:0;box-sizing:border-box}
html,body{width:1200px;height:923px;overflow:hidden;background:var(--bg)}
body{font-family:"Arimo",Arial,sans-serif;position:relative}
.brochure{position:absolute;left:94px;top:75px;width:1028px;height:790px;background:var(--paper);transform:scale(0.983);transform-origin:0 0;box-shadow:0 2px 8px rgba(0,0,0,.12)}
.panel{position:absolute;top:0;height:790px;width:343px}
.panel--left{left:0;border-right:1px solid var(--fold)}
.panel--middle{left:343px;border-right:1px solid var(--fold)}
.panel--right{left:686px;width:342px}
.heading{font-family:"Poiret One",sans-serif;color:var(--green-dark);font-size:31px;line-height:32px;text-align:center;font-weight:400;position:absolute;left:0;right:0;top:32px}
.heading.contact-heading{top:648px}
.features{position:absolute;left:20px;width:304px;list-style:none}
.features li{margin-bottom:13px}
.features h3{font-size:12.5px;font-weight:400;color:var(--green-dark);line-height:15px}
.features h3::before{content:"";display:inline-block;width:5px;height:5px;border-radius:50%;background:var(--green-dark);margin:0 9px 2px 2px;vertical-align:middle}
.features p{font-size:11px;line-height:14px;color:var(--body)}
.features--top{top:119px}
.features--bottom{top:469px}
.photo{position:absolute}
.photo--couple{left:17px;top:284px;width:306px;height:172px;background:linear-gradient(180deg,#e9e4dc 0%,var(--photo-a) 55%,#9a9185 100%)}
.photo--castle{left:14px;top:24px;width:313px;height:488px;background:linear-gradient(180deg,#f2efe9 0%,#b9ab98 40%,var(--photo-b) 100%)}
.section-tab{position:absolute;left:17px;width:304px;height:24px;border-bottom:2px solid var(--green-dark)}
.section-tab span{display:inline-block;background:var(--green-dark);color:#fff;font-size:13px;line-height:22px;padding:0 6px;width:88px;height:22px}
.copy{position:absolute;left:18px;width:305px;font-size:11.5px;line-height:16px;color:var(--body);text-align:justify;hyphens:auto;-webkit-hyphens:auto}
.copy p+p{margin-top:16px}
.contact{position:absolute;left:46px;top:699px;display:grid;grid-template-columns:47px auto;font-size:12px;line-height:23px}
.contact dt{color:var(--green-lite)}
.contact dd{color:var(--green-dark)}
.heart{position:absolute;left:16px;top:462px;width:310px;height:262px}
.brand{position:absolute;left:0;right:0;top:560px;text-align:center}
.brand-dot{display:inline-block;width:10px;height:10px;border-radius:50%;background:var(--green-lite);margin-bottom:8px}
.brand-name{font-family:"Poiret One",sans-serif;font-size:28px;line-height:34px;color:var(--green-dark)}
.tagline{position:absolute;left:14px;top:705px;width:313px;height:67px;background:var(--band);color:#fff;font-family:"Tinos",serif;font-style:italic;font-size:15.5px;line-height:18px;text-align:center;padding-top:16px}
</style>
</head>
<body>
<main class="brochure">

  <section class="panel panel--left">
    <h2 class="heading">What Makes Us<br>Different?</h2>
    <ul class="features features--top">
      <li><h3>Simple pricing</h3><p>What you see is the total cost of everything, not a complex breakdown that only an industry expert can decipher</p></li>
      <li><h3>No hidden surcharges</h3><p>The price we include is cleared defined and there are no credit card charges</p></li>
      <li><h3>Holidays designed around you</h3><p>Tell us what you want and we'll design the holiday to your needs</p></li>
    </ul>
    <div class="photo photo--couple" role="img" aria-label="Photo of a newlywed couple embracing on a stone bridge with an old city skyline behind"></div>
    <ul class="features features--bottom">
      <li><h3>Small is beautiful</h3><p>We a small family run business with an emphasis on a personal touch and flexibility</p></li>
      <li><h3>Community based approach</h3><p>We use small community based suppliers where possible to encourage social responsibility</p></li>
      <li><h3>Carbon off-setting</h3><p>We offset the carbon from both flights and car travel to help minimise net effect on the environment</p></li>
      <li><h3>Consumer protection</h3><p>Martha Bell will provide comprehensive set of insurances and bonding so you can continue your holiday or get a refund in the case of insolvency or ash clouds</p></li>
      <li><h3>Disabilities and minorities</h3><p>We have a clear policy on recruiting people from minorities and those with disabilities if they meet the requirements of the job</p></li>
    </ul>
  </section>

  <section class="panel panel--middle">
    <h2 class="heading">Luxury Holidays At<br>A Great Value</h2>

    <div class="section-tab" style="top:107px"><span>About Us</span></div>
    <div class="copy" style="top:143px"><p>Your comfort is our goal. Let us help you with planning your fantastic escape. We seek to provide you with a restful retreat that you can think of as your home away from home. We carbon offset your travel to help the environment. Consumer protection is provided as standard to cover you in case of nasty surprises such as ash clouds. We also try to source small and local accommodation rather than the large international organisations that dominate the industry.</p></div>

    <div class="section-tab" style="top:299px"><span>Our Travel</span></div>
    <div class="copy" style="top:335px"><p>Our holidays are tailored to your needs, and our rooms feature beautiful décor and all the amenities you could need. We have made it easy and safe to reserve and pay.</p></div>

    <div class="section-tab" style="top:395px"><span>Our Staff</span></div>
    <div class="copy" style="top:431px">
      <p>We believe in the small is beautiful concept.</p>
      <p>The company has two directors.</p>
      <p>We try to help our best and brightest at university by encouraging them to set up on their own and become our main Sales Representatives.</p>
      <p>This allows them to gain valuable experience and support whilst at university and provides us with the flexibility we need to compete against the big guns.</p>
    </div>

    <h2 class="heading contact-heading">Contact Us!</h2>
    <dl class="contact">
      <dt>web:</dt><dd>www.marthabellvoyages.co.uk</dd>
      <dt>email:</dt><dd>simon@marthabellvoyages.co.uk</dd>
      <dt>mobile:</dt><dd>07841296530</dd>
    </dl>
  </section>

  <section class="panel panel--right">
    <div class="photo photo--castle" role="img" aria-label="Photo of a bride and groom standing before a gothic cathedral and red-roofed old town"></div>
    <svg class="heart" viewBox="0 0 310 262" aria-hidden="true">
      <path d="M155 60 C130 10 60 0 25 40 C-10 80 5 140 45 180 C85 220 130 235 155 258 C180 235 225 220 265 180 C305 140 320 80 285 40 C250 0 180 10 155 60 Z" fill="#fff" stroke="var(--heart-edge)" stroke-width="7"/>
    </svg>
    <div class="brand">
      <span class="brand-dot"></span>
      <div class="brand-name">Martha Bell Voyages</div>
    </div>
    <p class="tagline">Personal Tailor-Made Honeymoons for<br>our Guests at a Lower Cost</p>
  </section>

</main>
</body>
</html>
```